Boutique Store Selling Antiques and Unique Finds

I need a Web Page designed for my Store Called "Larkmoor Lane". I would like a very classic, muted design that looks European when pulled up. I will be selling Antiques from all over the world and Unique finds that have reproduced. I will also be selling high-end purses and jewelry with unique, reasonable products for the every-day buyer as well.

Target Market(s)

25-70 year old men and women;)

Coding

Coded - Design and coding required

Number of Pages Required

1 page

Colors

Designer to choose only greyscale colors for use in the design.

Requirements
Must have
• I want it

```html
<!DOCTYPE html>
<html lang="en">
<head>
<meta charset="utf-8">
<title>Larkmoor Lane — Antiques &amp; Unique Finds</title>
<link href="https://fonts.googleapis.com/css2?family=Lora:wght@400&family=Questrial&display=swap" rel="stylesheet">
<style>
:root{
  --ink:#1c1a1b;
  --text:#2a2a2a;
  --line:#cfcfcf;
  --white:#ffffff;
  --hero-dark:#1e1813;
  --hero-mid:#5a4a3b;
  --stone:#cbbfae;
  --stone-light:#ddd4c7;
}
*{box-sizing:border-box;margin:0;padding:0}
html,body{width:1200px;height:2799px;overflow:hidden}
body{background:var(--white);font-family:"Lora",Georgia,serif;color:var(--text);position:relative}
a{color:inherit;text-decoration:none}

.top-bar{height:52px;background:var(--ink);color:#fff;font-size:15px;position:relative}
.top-bar .left{position:absolute;left:111px;top:16px;display:flex;gap:26px}
.top-bar .right{position:absolute;right:111px;top:16px;display:flex;gap:22px;align-items:center}
.top-bar svg{vertical-align:-2px}

.site-header{height:179px;position:relative}
.brand{position:absolute;left:0;right:0;top:48px;text-align:center;font-size:27px;letter-spacing:6px;text-transform:uppercase;color:var(--ink)}
.header-rule{position:absolute;left:111px;right:111px;top:113px;border-top:1px solid var(--line)}
.main-nav{position:absolute;left:0;right:0;top:136px;display:flex;justify-content:center;gap:92px;font-size:15px;text-transform:uppercase;color:var(--ink)}

.hero{height:699px;position:relative;
  background:
    radial-gradient(ellipse 30% 38% at 55% 58%,rgba(150,128,104,.75) 0%,rgba(110,92,74,.45) 55%,rgba(0,0,0,0) 100%),
    radial-gradient(ellipse 18% 40% at 20% 50%,rgba(120,98,74,.55) 0%,rgba(0,0,0,0) 100%),
    radial-gradient(ellipse 20% 25% at 90% 62%,rgba(130,106,74,.5) 0%,rgba(0,0,0,0) 100%),
    linear-gradient(180deg,#2a231d 0%,#3b3128 55%,#5a4636 80%,#3a2b22 100%)}
.hero-dots{position:absolute;left:0;right:0;top:675px;display:flex;justify-content:center;gap:8px}
.hero-dots span{width:10px;height:10px;border-radius:50%;background:#fff}
.hero-dots span.active{background:#8a8a8a}

.products{height:969px;position:relative}
.section-title{position:absolute;left:0;right:0;top:46px;text-align:center;font-size:39px;font-weight:400;color:var(--ink)}
.title-rule{position:absolute;left:579px;width:42px;top:101px;border-top:2px solid var(--ink)}
.product-grid{position:absolute;left:112px;top:134px;display:grid;grid-template-columns:repeat(4,232px);column-gap:17px;row-gap:52px}
.product-card{height:361px;background:#fff;box-shadow:0 0 4px rgba(0,0,0,.18);text-align:center;padding:9px 8px 0}
.product-image{height:185px}
.img-cases{background:linear-gradient(180deg,#6b5233 0%,#8c7a58 22%,#a08a66 32%,#3a2418 45%,#5a3524 70%,#2a1a14 100%)}
.img-stair{background:linear-gradient(90deg,#3a2116 0%,#6b3d26 35%,#8a5a3c 55%,#4a2a1c 75%,#2a1810 100%)}
.img-notions{background:linear-gradient(160deg,#6a5a48 0%,#a8987e 35%,#4a3e34 60%,#2a2420 100%)}
.img-medal{background:radial-gradient(ellipse 30% 50% at 50% 55%,#6a6a6e 0%,#8a8a86 40%,#c9c0b4 75%,#d8d0c6 100%)}
.img-books{background:linear-gradient(90deg,#3a2a1e 0%,#5a3a2a 25%,#6b2a2a 45%,#2a1e1a 65%,#4a3424 85%,#2a1e16 100%)}
.img-statue{background:radial-gradient(ellipse 35% 60% at 50% 65%,#cfc3ac 0%,#a8987e 40%,#4a2a1c 75%,#2a1810 100%)}
.img-plant{background:radial-gradient(ellipse 50% 55% at 50% 45%,#4a6a3a 0%,#2e4a26 45%,#8a8a86 80%,#c8c4c0 100%)}
.img-crown{background:linear-gradient(180deg,#d6c8b4 0%,#b9a28a 25%,#2a2422 45%,#34465e 62%,#b0a288 78%,#4a3a38 100%)}
.product-price{margin-top:25px;font-size:21px;color:var(--text)}
.product-name{margin-top:6px;font-size:18px;color:var(--text)}
.view-details{display:inline-block;margin-top:13px;width:137px;height:44px;line-height:42px;border:1px solid #b8b8b8;border-radius:22px;font-size:16px;color:var(--text)}

.feature{height:504px;position:relative;background:linear-gradient(90deg,var(--stone) 0%,var(--stone-light) 60%,#d3c9bc 100%)}
.feature-image{position:absolute;left:0;top:0;width:540px;height:504px;
  background:
    radial-gradient(ellipse 45% 30% at 48% 30%,rgba(170,132,70,.85) 0%,rgba(140,104,56,.5) 55%,rgba(0,0,0,0) 100%),
    linear-gradient(180deg,#d4cbc0 0%,#c6b8a4 15%,#a88a5a 35%,#3a302a 48%,#6a4a2e 62%,#4e3422 80%,#6a2a2a 88%,#d0c6ba 96%)}
.feature-copy{position:absolute;left:627px;top:135px;width:404px}
.feature-copy h2{font-weight:400;font-size:36px;color:#3a3532;white-space:nowrap}
.feature-copy p{margin-top:22px;font-family:Arial,Helvetica,sans-serif;font-size:14px;line-height:25.7px;color:#3a3532;text-align:justify}

.site-footer{height:396px;background:var(--ink);color:#fff;position:relative;font-family:"Questrial",Arial,sans-serif}
.footer-brand{position:absolute;left:111px;width:260px;top:128px;text-align:center;font-family:"Lora",Georgia,serif;font-size:22px;letter-spacing:4px;text-transform:uppercase}
.social{position:absolute;left:139px;top:182px;display:flex;gap:6px}
.social a{width:37px;height:37px;border:2px solid #fff;border-radius:50%;display:flex;align-items:center;justify-content:center;font-size:8px}
.footer-col h3{font-weight:400;font-size:21px;letter-spacing:.5px;text-transform:uppercase}
.quick-links{position:absolute;left:435px;top:57px}
.quick-links ul{list-style:none;margin-top:22px}
.quick-links li{font-size:12.5px;height:30px;display:flex;align-items:center;gap:12px;text-transform:uppercase}
.contact{position:absolute;left:631px;top:57px}
.contact-item{display:flex;align-items:flex-start;gap:14px;font-size:14.5px;line-height:24px;margin-top:12px}
.contact-item:first-of-type{margin-top:24px}
.contact-icon{width:36px;height:36px;border-radius:50%;background:#2c2a2b;display:flex;align-items:center;justify-content:center;flex:none}
.contact-item span{padding-top:6px}
.payments{position:absolute;left:877px;top:57px;width:215px}
.payments p{margin-top:24px;font-family:Arial,Helvetica,sans-serif;font-size:13.5px;line-height:24px}
.cards{display:flex;gap:3px;margin-top:16px}
.cards span{width:40px;height:27px;background:#fff;color:var(--ink);border-radius:3px;font-size:9px;display:flex;align-items:center;justify-content:center}
.copyright{position:absolute;left:0;right:0;top:359px;text-align:center;font-size:14.5px}
</style>
</head>
<body>

<div class="top-bar">
  <div class="left"><a href="#">My Account</a><span>|</span><a href="#">Check Out</a></div>
  <div class="right">
    <a href="#">Sign in</a>
    <a href="#"><svg width="14" height="13" viewBox="0 0 14 13"><path d="M0 1h2.5l2 7h7l2-5.5H4" fill="none" stroke="#fff" stroke-width="1.6"/><circle cx="5.5" cy="11" r="1.2" fill="#fff"/><circle cx="10.5" cy="11" r="1.2" fill="#fff"/></svg> Cart (0)</a>
    <svg width="14" height="14" viewBox="0 0 14 14"><circle cx="6" cy="6" r="4.3" fill="none" stroke="#fff" stroke-width="2"/><path d="M9 9l4 4" stroke="#fff" stroke-width="2.2"/></svg>
  </div>
</div>

<header class="site-header">
  <div class="brand">Larkmoor Lane</div>
  <div class="header-rule"></div>
  <nav class="main-nav"><a href="#">Home</a><a href="#">About Us</a><a href="#">Product</a><a href="#">Gallery</a><a href="#">Contact</a></nav>
</header>

<section class="hero" role="img" aria-label="Ornate carved metal elephant figurine among antique brass vessels on a patterned rug">
  <div class="hero-dots"><span></span><span class="active"></span><span></span></div>
</section>

<section class="products">
  <h2 class="section-title">Our Products</h2>
  <div class="title-rule"></div>
  <div class="product-grid">
    <div class="product-card"><div class="product-image img-cases" role="img" aria-label="Stacked vintage leather suitcases beneath a gilt mirror"></div><div class="product-price">$25.99</div><div class="product-name">Product Name</div><a class="view-details" href="#">View Details</a></div>
    <div class="product-card"><div class="product-image img-stair" role="img" aria-label="Wood-panelled staircase with a crystal chandelier and stone statue"></div><div class="product-price">$25.99</div><div class="product-name">Product Name</div><a class="view-details" href="#">View Details</a></div>
    <div class="product-card"><div class="product-image img-notions" role="img" aria-label="Compartment box of antique sewing notions"></div><div class="product-price">$25.99</div><div class="product-name">Product Name</div><a class="view-details" href="#">View Details</a></div>
    <div class="product-card"><div class="product-image img-medal" role="img" aria-label="Antique bronze medal on a blue ribbon"></div><div class="product-price">$25.99</div><div class="product-name">Product Name</div><a class="view-details" href="#">View Details</a></div>
    <div class="product-card"><div class="product-image img-books" role="img" aria-label="Row of old leather-bound books"></div><div class="product-price">$25.99</div><div class="product-name">Product Name</div><a class="view-details" href="#">View Details</a></div>
    <div class="product-card"><div class="product-image img-statue" role="img" aria-label="Carved stone statue in a wooden hall"></div><div class="product-price">$25.99</div><div class="product-name">Product Name</div><a class="view-details" href="#">View Details</a></div>
    <div class="product-card"><div class="product-image img-plant" role="img" aria-label="Leafy green plant in a silver urn"></div><div class="product-price">$25.99</div><div class="product-name">Product Name</div><a class="view-details" href="#">View Details</a></div>
    <div class="product-card"><div class="product-image img-crown" role="img" aria-label="Jewelled fur crown resting on a stack of books"></div><div class="product-price">$25.99</div><div class="product-name">Product Name</div><a class="view-details" href="#">View Details</a></div>
  </div>
</section>

<section class="feature">
  <div class="feature-image" role="img" aria-label="Gilded star crown resting on antique books against marble"></div>
  <div class="feature-copy">
    <h2>Antiques &amp; Unique Finds</h2>
    <p>Sed ut perspiciatis unde omnis iste natus error sit voluptatem accusantium doloremque laudantium, totam rem aperiam, eaque ipsa quae ab illo inventore veritatis et quasi architecto beatae vitae dicta sunt explicabo. Nemo enim ipsam voluptatem quia voluptas sit aspernatur aut odit aut fugit, sed quia consequuntur magni dolores eos qui ratione voluptatem sequi nesciunt.</p>
  </div>
</section>

<footer class="site-footer">
  <div class="footer-brand">Larkmoor Lane</div>
  <div class="social"><a href="#">Folio</a><a href="#">Chirp</a><a href="#">Snap</a><a href="#">Linker</a><a href="#">Reel</a></div>

  <div class="footer-col quick-links">
    <h3>Quick Links</h3>
    <ul>
      <li><svg width="16" height="8" viewBox="0 0 16 8"><path d="M0 4h15M11 1l4 3-4 3" fill="none" stroke="#fff"/></svg>Home</li>
      <li><svg width="16" height="8" viewBox="0 0 16 8"><path d="M0 4h15M11 1l4 3-4 3" fill="none" stroke="#fff"/></svg>About Us</li>
      <li><svg width="16" height="8" viewBox="0 0 16 8"><path d="M0 4h15M11 1l4 3-4 3" fill="none" stroke="#fff"/></svg>Product</li>
      <li><svg width="16" height="8" viewBox="0 0 16 8"><path d="M0 4h15M11 1l4 3-4 3" fill="none" stroke="#fff"/></svg>Gallery</li>
      <li><svg width="16" height="8" viewBox="0 0 16 8"><path d="M0 4h15M11 1l4 3-4 3" fill="none" stroke="#fff"/></svg>Contact</li>
    </ul>
  </div>

  <div class="footer-col contact">
    <h3>Contact Us</h3>
    <div class="contact-item"><div class="contact-icon"><svg width="13" height="13" viewBox="0 0 13 13"><path d="M2 1l2.5 0 1 3-1.5 1a7 7 0 0 0 4 4l1-1.5 3 1v2.5c0 .5-.5 1-1 1C5.5 12 1 7.5 1 2c0-.5.5-1 1-1z" fill="#fff"/></svg></div><span>000-121-1231</span></div>
    <div class="contact-item"><div class="contact-icon"><svg width="13" height="10" viewBox="0 0 13 10"><rect x=".5" y=".5" width="12" height="9" fill="none" stroke="#fff"/><path d="M.5 .5l6 5 6-5" fill="none" stroke="#fff"/></svg></div><span>info@company.com</span></div>
    <div class="contact-item"><div class="contact-icon"><svg width="10" height="13" viewBox="0 0 10 13"><path d="M5 12S1 7 1 4.5a4 4 0 0 1 8 0C9 7 5 12 5 12z" fill="#fff"/><circle cx="5" cy="4.5" r="1.4" fill="#2c2a2b"/></svg></div><span>2172 Lorem Ipsum<br>dummy text 32308</span></div>
  </div>

  <div class="footer-col payments">
    <h3>Payments</h3>
    <p>Sed ut perspiciatis unde omnis us error sit voluptatem</p>
    <div class="cards"><span>Cardo</span><span>Orbit</span><span>Amplo</span><span>Vanta</span><span>Paywell</span></div>
  </div>

  <div class="copyright">© Copyrights 2021-Larkmoor Lane.All Rights Reserved.</div>
</footer>

</body>
</html>
```